Flyer-Design für Psychotherapeut
Zielgruppe
Angeboten wird als Dienstleistung Psychotherapie, Coaching und Paarberatung
für Einzelpersonen (Männer/Frauen), Paare und Familien in schwierigen privaten und beruflichen Lebenssituationen.
Aufgabenstellung
Sehr geehrte Damen, sehr geehrte Herren,
gewünscht wird ein Falzflyer Hochformat, DIN-Lang, Wickelfalz, 6 bedruckte Seiten mit dem Endformat 10,0 x 21,0 cm. Ein entsprechendes Datenblatt der Druckerei finden Sie im Anhang.
Der Flyer wird auf einer Gesundheitsmesse eingesetzt und soll einen Überblick über mein Dienstleistungsangebot geben.
In der beigefügten Word Datei finden Sie einen von mir erstellten Flyer-Text-Entwurf. Er soll lediglich als Orientierung dienen. Weitere Infos erhalten Sie auf meiner Homepage
www.praxis-tollring-quast.de.
Desweiteren erhalten Sie ein hochgeladenes Foto von mir, welches Sie bitte in Ihren Entwurf mit einbinden.
Ich bitte um Vorschläge für ein professionelles Design mit moderener gut lesbarer Schrift sowie farblich abgestimmten Blöcken des Inhalts.
Besonders wichtig ist mir die Orientierung an meinen Logofarben.
Das Logo wurde auch von gestaltwerk.de erstellt. Sie finden es unter meinen Projekten.
Für Rückfragen stehe ich Ihnen gerne zur Verfügung.
Freundliche Grüße
Sabine Tollring-Quast

```html
<!DOCTYPE html>
<html lang="de">
<head>
<meta charset="utf-8">
<title>Falzflyer Sabine Tollring-Quast</title>
<link href="https://fonts.googleapis.com/css2?family=Exo+2:wght@300;400;600;700&display=swap" rel="stylesheet">
<style>
:root{
  --orange:#e5521c;
  --orange-light:#f28a2e;
  --peach:#f9c6a6;
  --peach-soft:#fde6d8;
  --grey-text:#555;
  --grey-dark:#5a5a5a;
  --stage:#3f4652;
  --white:#fff;
}
*{margin:0;padding:0;box-sizing:border-box}
html,body{width:1200px;height:1038px;overflow:hidden;background:var(--stage)}
body{position:relative;font-family:"Exo 2",sans-serif;color:var(--grey-text)}
.sheet{position:absolute;width:1130px;height:799px;background:var(--white);overflow:hidden;transform-origin:0 0;transform:scale(0.5796);box-shadow:0 6px 20px rgba(0,0,0,.35)}
.sheet--outside{left:246px;top:43px}
.sheet--inside{left:248px;top:527px}
.abs{position:absolute}
.photo{position:absolute}
.band{position:absolute;left:0;top:0;width:1130px;height:300px;pointer-events:none}
.peach{position:absolute;background:linear-gradient(180deg,var(--peach) 0%,var(--peach-soft) 45%,var(--white) 100%)}
.h-main{font-weight:700;font-size:25px;color:var(--orange);letter-spacing:.2px}
.h-sub{font-weight:400;font-size:17px;line-height:23px;color:var(--orange);text-transform:uppercase}
.ticks{list-style:none;font-size:12.5px;line-height:16px;color:var(--grey-text)}
.ticks li{position:relative;padding-left:26px;margin-bottom:9px}
.ticks li::before{content:"✔";position:absolute;left:0;top:-1px;color:var(--orange);font-size:15px}
.ticks--tight li{margin-bottom:7px}
.copy{font-size:12.5px;line-height:16px;text-align:justify}
.copy p{margin-bottom:14px}
.contact{font-size:12.5px;line-height:16px}
.contact p{margin-bottom:11px}
.callout{position:absolute;left:537px;top:217px;width:164px;height:164px;border-radius:50%;background:radial-gradient(circle at 40% 35%,var(--orange-light),var(--orange));border:5px solid rgba(255,255,255,.75);display:flex;align-items:center;justify-content:center}
.callout span{display:block;transform:rotate(-12deg);color:var(--white);font-weight:600;font-size:16px;line-height:19px;text-align:center}
.portrait{position:absolute;left:418px;top:336px;width:108px;height:108px;border-radius:12px;background:linear-gradient(160deg,#d8d8d8,#8e8e8e)}
.brand{position:absolute;left:770px;top:38px;display:flex;align-items:center;gap:16px}
.brand-dot{width:58px;height:58px;border-radius:50%;background:var(--orange);flex:none}
.brand-name{font-weight:300;font-size:26px;color:var(--grey-dark);line-height:28px}
.brand-line{font-size:12.5px;color:var(--orange);margin-top:4px}
.headline{position:absolute;left:750px;top:525px;width:380px;text-align:center;font-size:35px;line-height:46px;font-weight:400;color:var(--grey-dark)}
.headline b{color:var(--orange);font-weight:700}
.tagline{position:absolute;left:793px;top:690px;font-size:25px;line-height:38px;color:var(--orange)}
.url{position:absolute;right:467px;top:760px;font-weight:700;font-size:20px;color:var(--orange)}
.rule{position:absolute;left:0;top:753px;width:663px;height:1.5px;background:var(--orange)}
</style>
</head>
<body>

<!-- Outside of the fold: back panel, inside flap, cover -->
<section class="sheet sheet--outside">
  <div class="photo" role="img" aria-label="Foto: lächelndes Paar auf einem Sofa" style="left:0;top:0;width:369px;height:278px;background:linear-gradient(160deg,#bcc6cc,#8fa3b5 45%,#cfd9a8)"></div>
  <div class="photo" role="img" aria-label="Foto: geöffnete Hände mit Fragezeichen" style="left:369px;top:0;width:381px;height:278px;background:linear-gradient(150deg,#cfe3f2,#8fb6d8 55%,#e9c8b6)"></div>
  <div class="peach" style="left:0;top:278px;width:750px;height:475px"></div>
  <div class="photo" role="img" aria-label="Foto: hölzerne Treppe in grüner Natur" style="left:750px;top:100px;width:380px;height:420px;background:linear-gradient(180deg,#9fb07a,#9c7650 45%,#7a5a3c)"></div>
  <div class="abs" style="left:750px;top:505px;width:380px;height:135px;background:linear-gradient(180deg,#d6d1cd,#f3f0ee)"></div>

  <svg class="band" viewBox="0 0 1130 300" aria-hidden="true">
    <path d="M0 0H1130V25Q620 0 0 95Z" fill="#e8501b"/>
    <path d="M0 95Q560 10 1130 40V0H0Z" fill="url(#g1)" opacity=".9"/>
    <defs><linearGradient id="g1" x1="0" x2="1"><stop offset="0" stop-color="#e5521c"/><stop offset=".6" stop-color="#f07c26"/><stop offset="1" stop-color="#e8501b"/></linearGradient></defs>
    <path d="M0 115Q560 20 1130 55" stroke="#fff" stroke-width="2" fill="none"/>
    <path d="M0 102Q560 14 1130 30" stroke="#f3b08a" stroke-width="1.5" fill="none"/>
    <path d="M750 30Q940 32 1130 55V100L750 100Z" fill="#fff"/>
    <path d="M750 105Q950 100 1130 170V95H750Z" fill="#fff"/>
    <path d="M750 108Q950 100 1130 168" stroke="#e5521c" stroke-width="2" fill="none"/>
    <path d="M750 288Q560 296 369 278" stroke="none" fill="none"/>
  </svg>
  <svg class="abs" style="left:750px;top:480px" width="380" height="190" aria-hidden="true">
    <path d="M0 30Q190 0 380 20" stroke="#e5521c" stroke-width="2" fill="none"/>
    <path d="M0 160Q190 190 380 150V190H0Z" fill="#fff"/>
    <path d="M0 160Q190 190 380 150" stroke="#e5521c" stroke-width="3" fill="none"/>
  </svg>

  <div class="abs" style="left:48px;top:293px;width:310px">
    <h2 class="h-main">PAARBERATUNG –</h2>
    <h3 class="h-sub" style="margin-top:12px">Unterstützung für Paare<br>in Krisenzeiten</h3>
    <ul class="ticks" style="margin-top:14px">
      <li>Wenn Sie das Gefühl haben aneinander vorbei zu reden.</li>
      <li>Wenn Ihr Beziehungsalltag von Streitereien und Konflikten bestimmt wird.</li>
      <li>Wenn Sie Ihre gemeinsame Intimität und Sexualität verloren haben</li>
      <li>Wenn eine Affäre Ihre Beziehung erschüttert hat.</li>
      <li>Wenn nach der Geburt von Kindern, durch Arbeitslosigkeit oder Krankheit Probleme in Ihrer Beziehung entstanden sind</li>
      <li>Wenn das Leben in der Patchwork-Familie Ihre Beziehung belastet</li>
    </ul>
    <h3 class="h-sub" style="margin-top:24px">Trennungsbegleitung<br>und Mediation</h3>
    <ul class="ticks" style="margin-top:14px"><li>Wenn Sie über Trennung nachdenken.</li></ul>
  </div>

  <div class="portrait" role="img" aria-label="Porträtfoto der Therapeutin"></div>
  <div class="callout"><span>Haben Sie Fragen?<br>Rufen Sie mich an.<br>Ich bin für Sie da.</span></div>

  <div class="abs contact" style="left:418px;top:460px;width:300px">
    <p><b style="color:var(--orange);font-size:14px">SABINE TOLLRING-QUAST</b><br>Heilpraktikerin Psychotherapie (HeilprG)<br>Systemischer Coach (VSCB)</p>
    <p>Am Lindenhang 14<br>64397 Mühlbrunn</p>
    <p>Telefon 06150 – 472913<br>info@praxis-tollring-quast.de</p>
    <p style="margin-top:18px">Rufen Sie mich an. Ich bin für Sie da!<br>Ich freue mich auf Ihren Besuch!</p>
    <h3 class="h-sub" style="margin-top:28px;line-height:20px">Weitere Informationen</h3>
    <p style="font-size:14.5px;line-height:17px">über mich und meine Angebote finden<br>Sie auf meiner Homepage.</p>
  </div>
  <div class="rule"></div>
  <div class="url">www.praxis-tollring.de</div>

  <div class="brand">
    <div class="brand-dot"></div>
    <div><div class="brand-name">Sabine Tollring-Quast</div><div class="brand-line">Psychotherapie &nbsp;|&nbsp; Coaching &nbsp;|&nbsp; Paarberatung</div></div>
  </div>
  <div class="headline">AUS<b>WEGE</b><br>LÖSUNGS<b>WEGE</b></div>
  <div class="tagline">Für mehr Zufriedenheit<br>im Privatleben und Beruf</div>
</section>

<!-- Inside of the fold: three content panels -->
<section class="sheet sheet--inside">
  <div class="photo" role="img" aria-label="Foto: gestresste Frau am Laptop" style="left:0;top:20px;width:380px;height:262px;background:linear-gradient(150deg,#c9d3cf,#9fb0a8 50%,#e4e1dc)"></div>
  <div class="peach" style="left:0;top:282px;width:380px;height:517px"></div>
  <div class="peach" style="left:380px;top:85px;width:750px;height:714px"></div>
  <svg class="band" viewBox="0 0 1130 300" aria-hidden="true">
    <defs><linearGradient id="g2" x1="0" x2="1"><stop offset="0" stop-color="#e5521c"/><stop offset=".6" stop-color="#f07c26"/><stop offset="1" stop-color="#e8501b"/></linearGradient></defs>
    <path d="M0 0H1130V50Q620 0 0 110Z" fill="url(#g2)"/>
    <path d="M380 26H760V88Q570 84 380 96Z" fill="#c9b3a4"/>
    <path d="M0 118Q560 35 1130 55" stroke="#fff" stroke-width="2" fill="none"/>
    <path d="M380 96Q570 84 760 90" stroke="#e5521c" stroke-width="2" fill="none"/>
  </svg>

  <div class="abs" style="left:48px;top:300px;width:310px">
    <h2 class="h-main">SIE WÜNSCHEN SICH ...</h2>
    <h3 class="h-sub" style="margin-top:12px">Entlastung und<br>positive Veränderung weil ...</h3>
    <ul class="ticks" style="margin-top:14px">
      <li>Sie sich in einer akuten privaten oder beruflichen Krisensituation befinden.</li>
      <li>Sie Probleme in Ihrer Partnerschaft haben.</li>
      <li>Sie mit Stress besser umgehen wollen.</li>
      <li>Sie sich antriebslos- und lustlos, erschöpft oder ständig überfordert fühlen.</li>
      <li>Sie unter Ängsten oder Panikattacken leiden, die Sie belasten und einschränken.</li>
    </ul>
    <div class="copy" style="margin-top:46px">
      <p>Jeder Mensch kommt im Leben in Situationen, die Unzufriedenheit, Überforderung und seelische Belastungen auslösen.</p>
      <p>Wenn Veränderung nicht alleine gelingt, können Psychotherapie, Coaching oder Paarberatung eine große Hilfe sein, um Lösungswege aus diesen belastenden Situationen zu finden.</p>
    </div>
  </div>

  <div class="abs" style="left:420px;top:108px;width:292px">
    <h2 class="h-main">MEIN ANGEBOT FÜR SIE</h2>
    <h3 class="h-sub" style="margin-top:14px">Beratung- und Gesprächs-<br>therapie nach Carl Rodewald</h3>
    <h3 class="h-sub" style="margin-top:14px">Systemisches Coaching und<br>Paarberatung</h3>
    <div class="copy" style="margin-top:14px">
      <p>Als erfahrene Therapeutin, Beraterin und Coach begleite ich Sie als Einzelperson, Paar oder Familie in schwierigen Lebenssituationen und Neuorientierungsphasen.</p>
      <p>Ich unterstütze Sie einfühlsam und lösungsorientiert. Dabei nutze ich anerkannte, wirksame Therapie- und Beratungsmethoden, die ich gemeinsam mit Ihnen, auf Ihre persönlichen Bedürfnisse und Ziele abstimme.</p>
      <p>Im Mittelpunkt stehen Sie mit Ihrem Anliegen.</p>
      <p>Wir begegnen uns in einer Atmosphäre der Wertschätzung, Anteilnahme und absoluten Diskretion.</p>
    </div>
    <h2 class="h-main" style="margin-top:22px">SIE KÖNNEN ...</h2>
    <ul class="ticks ticks--tight" style="margin-top:16px">
      <li>Bewältigungsstrategien entwickeln</li>
      <li>Ihre Fähigkeiten und Stärken entdecken</li>
      <li>Innere Blockaden überwinden</li>
      <li>Ihr Selbstvertrauen steigern</li>
      <li>Sich mutig und motiviert an Neues heranwagen</li>
      <li>Ihre Ziele umsetzen</li>
      <li>Ihr Leben und Ihre Partnerschaft so gestalten, wie Sie es sich wünschen.</li>
    </ul>
  </div>

  <div class="abs" style="left:797px;top:42px;width:310px">
    <h2 class="h-main">PSYCHOTHERAPIE</h2>
    <h3 class="h-sub" style="margin-top:12px">Meine Behandlungsschwerpunkte:</h3>
    <ul class="ticks ticks--tight" style="margin-top:14px">
      <li>Ängste- und Panikattacken</li>
      <li>Depression</li>
      <li>Erschöpfung/Burnout</li>
      <li>Reaktion auf schwere Belastungen</li>
      <li>Psychosomatische Beschwerden</li>
      <li>Psychoonkologie</li>
      <li>Mühlbrunner Gesundheitstraining</li>
    </ul>
    <h2 class="h-main" style="margin-top:28px">COACHING</h2>
    <h3 class="h-sub" style="margin-top:12px">Begleitung in Veränderung-<br>sprozessen und schwierigen<br>Lebensphasen/-krisen</h3>
    <ul class="ticks ticks--tight" style="margin-top:14px">
      <li>Veränderte Rahmenbedingungen im Privat- und Berufsleben wie z.B. Krankheit, Trennung, Trauer, Mobbing, Arbeitsplatzverlust u.a.</li>
      <li>Berufliche Neuorientierung</li>
      <li>Entscheidungsfindung</li>
      <li>Zielsetzung und Realisierung</li>
      <li>Lebensumbrüche wie z.B. Wechseljahre, Pensionierung u.a.</li>
    </ul>
    <h3 class="h-sub" style="margin-top:18px">Persönlichkeitsentwicklung</h3>
    <ul class="ticks ticks--tight" style="margin-top:14px">
      <li>Konflikte erkennen und konstruktiv lösen</li>
      <li>Beziehungs- und Lebensgestaltung</li>
      <li>Eigene Stärken entdecken, weiter entwickeln und nutzen</li>
      <li>Stressbewältigung/Burnoutprävention</li>
    </ul>
  </div>
</section>

</body>
</html>
```